Bestseller Novel Needs 2nd Cover Option

EXISTING BESTSELLER NEEDS REDESIGNED COVER.
BOOK: THE LAMPS WENT OUT
AUTHOR: MORVEN TULK
WHERE? It's for sale now on Brindlemart.com and Brindlemart.co.uk and is selling well. It's in the top 30 of its category.
NOTE: Make your design as final as you can, because if you are chosen then I will want to run the cover straight away. I am working to limited timing due to Chatterloom.
DETAILS
My bestselling novel 'The Lamps Went Out' (check it on Brindlemart please) has a beautiful and very successful cover already! It is selling high volumes and has taken only 9 days to get into the bestsellers in UK and USA.
However, I use Chatterloom advertising every day, and Chatterloom will no longer allow me to use the picture of the embryo (baby). This is because many Chatterloom users say they don't want to see an embryo on their Chatterloom page.
**How to Change the Cover**
Tips for Designers
YOU MAY USE (but you don't have to!) the deep red colour already present in the original cover; OR YOU MAY COME UP WITH A COMPLETELY NEW DESIGN WITH NEW COLOURS, PHOTOS ETC; CREATIVITY IS WELCOME. However, I'm happy too, if you wish to take the existing cover and simply try and create similar but replacing the problem part of the design (the baby).
DO extend your design to include the back cover and spine but of course for the Leafpad version, I need to have a front cover that can stand alone too. So you'll need to give me a) front cover only and b) Front cover, spine and back.
YOU MAY USE (but don't have to) the type of font present -- or something with a similar look -- in the original cover and the size of the fonts/relativity to each other;
YOU MUST KEEP the name of the book in the same positioning as on the original cover. One of the reasons is because in order to advertise on Chatterloom with a section of the new cover, I need to be able to crop out a clean square free of text which I will then be able to use in the Chatterloom ads. So the centre of the cover must be free of text.
**YOU MUST ENSURE the book looks like a psychological thriller/suspense novel!**
YOU MAY TRY to (but don't have to!) retain the same sort of background. If you look closely you will see that the background represents a park, tree or wintry scene. However your own design *may* elect to represent trees and parkland/winter more strongly and evocatively.
You can play around with these ideas. For example you might have the trees coming inwards towards the central character in a threatening way, conveying that this is a suspense/thriller novel or you may choose to keep them fine and very subtle as the original designer did.
YOU MAY CONSIDER including a figure of a female, faceless/face hidden, aged in late 20s, slim, long dark hair as the chief protagonist. It must not look in any way a 'romantic' presentation, as the young woman in the novel is very psychologically disturbed. YOU DO NOT HAVE TO FEATURE THIS FEMALE FIGURE IN YOUR DESIGN: I AM OPEN TO NEW IDEAS AROUND THE BOOK'S THEMES BUT YOU NEED TO USE THE KEY ELEMENTS OF THE BACKGROUND AND FONT.
*IF* YOU CHOOSE TO USE THE FEMALE IMAGE:
DO position your woman either walking through a park/wooded area OR seated on a park bench. Your choice.
IF the woman has her baby with her, the baby is in her arms, never a baby carriage or stroller.
ENSURE the finished image looks desolate, isolated, alone, lonely, dejected, sad, tormented, anxious, moody, evocative.... etc. Those are key feelings I wish to convey, play with them!
DO show a stark, unfriendly, hostile, winter scene. Leaves and bare trees are vital.
REMEMBER your woman -- if you use a woman in your designs -- has no visible facial expressions. It is important in suspense novels that the chief protagonist is not too finely defined because then, people can struggle to identify with them. So, her face might be turned away, or her head is looking down to the baby or across into the distance but in any case we cannot see her facial features.
DO replicate the main font (AS GIVEN BY FIRST DESIGNER) for the title and the author name. You may change the font for the strapline/blurb since this was added by me and does not show up well on the cover anyway.
Target Market(s)
Males and females 25-49 UK and USA/global. Readers of psychological thrillers.
Industry/Entity Type
Book Publisher
Font styles to use
Other font styles liked:
- Already shown. See brief.
Look and feel
Each slider illustrates characteristics of the customer's brand and the style your logo design should communicate.

```html
<!DOCTYPE html>
<html lang="en">
<head>
<meta charset="utf-8">
<title>The Lamps Went Out – Front Cover</title>
<link rel="stylesheet" href="https://fonts.googleapis.com/css2?family=Special+Elite&family=Courier+Prime:wght@700&family=Source+Sans+3:wght@400;500&display=block">
<style>
  :root {
    --stage: #d9d6d2;
    --cover-ground: #1c0306;
    --title-red: #b0121b;
    --tagline-yellow: #f3e31f;
    --fire-core: #ffe44a;
    --fire-mid: #f06a12;
    --fire-deep: #a3140c;
    --fire-edge: #2a0405;
  }
  * { margin: 0; padding: 0; box-sizing: border-box; }
  html, body {
    width: 1200px;
    height: 800px;
    overflow: hidden;
    background: var(--stage);
  }
  .stage {
    position: relative;
    width: 1200px;
    height: 800px;
  }
  .cover {
    position: absolute;
    left: 337px;
    top: 30px;
    width: 526px;
    height: 740px;
    background: var(--cover-ground);
    box-shadow: 0 10px 30px rgba(0,0,0,0.35);
    overflow: hidden;
  }
  .cover-art {
    position: absolute;
    left: 0;
    top: 0;
    width: 100%;
    height: 318px;
    background:
      radial-gradient(ellipse 38% 55% at 50% 58%, var(--fire-core) 0%, var(--fire-mid) 40%, transparent 75%),
      radial-gradient(ellipse 70% 60% at 50% 55%, var(--fire-deep) 0%, var(--fire-deep) 45%, transparent 85%),
      linear-gradient(180deg, var(--fire-edge) 0%, #5a0a08 35%, #6e0f0a 70%, var(--fire-edge) 100%);
  }
  .cover-art::after {
    content: "";
    position: absolute;
    left: 0; right: 0; bottom: 0;
    height: 40px;
    background: linear-gradient(180deg, transparent, var(--cover-ground));
  }
  .tagline {
    position: absolute;
    top: 336px;
    left: 0;
    width: 100%;
    text-align: center;
    font-family: "Source Sans 3", sans-serif;
    font-size: 16.5px;
    line-height: 21px;
    color: var(--tagline-yellow);
  }
  .title {
    position: absolute;
    left: 0;
    top: 0;
    width: 526px;
    height: 740px;
  }
  .title-word {
    font-family: "Special Elite", "Courier Prime", serif;
    fill: var(--title-red);
  }
  .author {
    position: absolute;
    top: 688px;
    left: 0;
    width: 100%;
    text-align: center;
    font-family: "Source Sans 3", sans-serif;
    font-weight: 500;
    font-size: 23px;
    letter-spacing: 14px;
    padding-left: 14px;
    color: var(--tagline-yellow);
  }
</style>
</head>
<body>
  <main class="stage">
    <article class="cover">
      <div class="cover-art" role="img" aria-label="Silhouette of a lone woman walking through dark bare trees against a blazing red and yellow fiery glow"></div>
      <p class="tagline">She was nothing. He was everything.<br>What would happen if their worlds collided ?</p>
      <h1 class="title-heading">
        <svg class="title" viewBox="0 0 526 740" role="img" aria-label="The Lamps Went Out">
          <text class="title-word title-the" x="37" y="507" font-size="128" textLength="233" lengthAdjust="spacingAndGlyphs">The</text>
          <text class="title-word title-lamps" x="176" y="550" font-size="50" textLength="112" lengthAdjust="spacingAndGlyphs">lamps</text>
          <text class="title-word title-went" x="298" y="562" font-size="120" textLength="200" lengthAdjust="spacingAndGlyphs">WENT</text>
          <text class="title-word title-out" x="128" y="653" font-size="108" textLength="270" lengthAdjust="spacingAndGlyphs">OUT</text>
        </svg>
      </h1>
      <p class="author">MORVEN TULK</p>
    </article>
  </main>
</body>
</html>
```